Hall of Fame annnouncement graphic for social media

I need a social media Hall of Fame announcement designed in the styles of some of the examples I've posted. I have attached the two gentlemens head shots ... the names are Dale Prosser and Jim Harnden

It is for the BRIARWOOD LINKS HONOR SOCIETY also include 2026 Inductees ... I have also attached the logo... make the post in similar colors as the logo.

I need this tomorrow so I am going to pick a winner in the next 24 hours.

```html
<!DOCTYPE html>
<html lang="en">
<head>
<meta charset="utf-8">
<title>Briarwood Links Honor Society – 2026 Inductees</title>
<link rel="stylesheet" href="https://fonts.googleapis.com/css2?family=Oswald:wght@400;500;600;700&display=swap">
<style>
  :root {
    --navy: #0b2a7d;
    --red: #b81c0e;
    --white: #ffffff;
    --stage: #5a5a5a;
    --sky-light: #f4f4f4;
    --sky-mid: #cfcfcf;
    --turf: #bdbdbd;
  }
  * { margin: 0; padding: 0; box-sizing: border-box; }
  html, body {
    width: 1200px; height: 741px; overflow: hidden;
    background: var(--stage);
  }
  .stage {
    position: absolute; left: 0; top: 0;
    width: 1215px; height: 750px;
    transform: scale(0.98765); transform-origin: 0 0;
    background: linear-gradient(135deg, #6a6a6a 0%, #4e4e4e 60%, #3c3c3c 100%);
  }
  .post {
    position: absolute; left: 77px; top: 66px;
    width: 1060px; height: 596px; overflow: hidden;
    font-family: "Oswald", "Arial Narrow", sans-serif;
  }
  .course-scene {
    position: absolute; inset: 0;
    background:
      radial-gradient(ellipse 55% 70% at 25% 45%, rgba(255,255,255,0.95) 0%, rgba(255,255,255,0.6) 55%, rgba(255,255,255,0) 100%),
      linear-gradient(180deg, var(--sky-light) 0%, #e2e2e2 35%, var(--sky-mid) 55%, #d8d8d8 70%, var(--turf) 100%);
  }
  .brand {
    position: absolute; left: 78px; top: 54px; width: 345px;
    text-align: center; color: var(--navy);
    font-weight: 700; text-transform: uppercase; line-height: 1.05;
  }
  .brand__line1 { display: block; font-size: 38px; letter-spacing: 1px; }
  .brand__line2 { display: block; font-size: 32px; letter-spacing: 3px; }
  .headline {
    position: absolute; left: 81px;
    color: var(--navy); font-weight: 700; line-height: 1;
    text-transform: uppercase; white-space: nowrap;
    transform-origin: 0 0;
  }
  .headline--top { top: 173px; font-size: 132px; transform: scaleX(0.74); }
  .headline--bottom { top: 290px; font-size: 190px; transform: scaleX(0.9); }
  .inductee-year {
    position: absolute; left: 81px; top: 490px; width: 340px;
    display: flex; align-items: center; gap: 14px;
    color: var(--red); font-size: 27px; font-weight: 500;
    text-transform: uppercase; white-space: nowrap;
  }
  .inductee-year::before, .inductee-year::after {
    content: ""; flex: 1; height: 2px; background: var(--red);
  }
  .inductee { position: absolute; top: 100px; width: 245px; height: 426px; }
  .inductee--first { left: 486px; }
  .inductee--second { left: 759px; }
  .inductee__backdrop { position: absolute; left: 0; top: 56px; width: 245px; height: 290px; }
  .inductee__photo {
    position: absolute; left: 28px; top: 8px; width: 189px; height: 338px;
    border-radius: 90px 90px 0 0;
    background: linear-gradient(180deg, #d9d9d9 0%, #ececec 45%, #f7f7f7 100%);
  }
  .inductee__label {
    position: absolute; left: 0; bottom: 0; width: 245px; height: 80px;
    background: var(--red); color: var(--white);
    border-left: 9px solid var(--navy); border-right: 9px solid var(--navy);
    text-align: center; text-transform: uppercase; white-space: nowrap;
    display: flex; flex-direction: column; justify-content: center;
  }
  .inductee__name { font-size: 27px; font-weight: 600; line-height: 1.15; }
  .inductee__club { font-size: 16px; font-weight: 400; line-height: 1.3; }
  .accent-bar { position: absolute; left: 0; bottom: 0; width: 1060px; height: 10px; display: flex; }
  .accent-bar span { height: 100%; }
  .accent-bar .blue-a { width: 82px; background: var(--navy); }
  .accent-bar .red { width: 338px; background: var(--red); }
  .accent-bar .blue-b { flex: 1; background: var(--navy); }
</style>
</head>
<body>
<div class="stage">
  <div class="post">
    <div class="course-scene" role="img" aria-label="Black and white golf course landscape with rolling fairways, bunkers, trees and a cloudy sky"></div>

    <div class="brand">
      <span class="brand__line1">Briarwood Links</span>
      <span class="brand__line2">Honor Society</span>
    </div>

    <div class="headline headline--top">Hall of</div>
    <div class="headline headline--bottom">Fame</div>
    <div class="inductee-year">2026 Inductees</div>

    <div class="inductee inductee--first">
      <svg class="inductee__backdrop" viewBox="0 0 245 290" aria-hidden="true">
        <defs>
          <linearGradient id="panelShade" x1="0" y1="0" x2="1" y2="1">
            <stop offset="0" stop-color="#3f3f3f"/>
            <stop offset="1" stop-color="#767676"/>
          </linearGradient>
        </defs>
        <polygon points="0,34 245,0 245,290 0,290" fill="url(#panelShade)"/>
      </svg>
      <div class="inductee__photo" role="img" aria-label="Head and shoulders portrait of inductee Dale Prosser in a white polo shirt"></div>
      <div class="inductee__label">
        <span class="inductee__name">Dale Prosser</span>
        <span class="inductee__club">Cedar Hollow Golf Course</span>
      </div>
    </div>

    <div class="inductee inductee--second">
      <svg class="inductee__backdrop" viewBox="0 0 245 290" aria-hidden="true">
        <polygon points="0,0 245,34 245,290 0,290" fill="url(#panelShade)"/>
      </svg>
      <div class="inductee__photo" role="img" aria-label="Head and shoulders portrait of inductee Jim Harnden in a light pink polo shirt"></div>
      <div class="inductee__label">
        <span class="inductee__name">Jim Harnden</span>
        <span class="inductee__club">Stonebridge Golf Club</span>
      </div>
    </div>

    <div class="accent-bar"><span class="blue-a"></span><span class="red"></span><span class="blue-b"></span></div>
  </div>
</div>
</body>
</html>
```